Brimble Diecast Torvel Collectables Website

looking for a vibrant web site marketplace built for diecast car enthusiasts to buy, sell, and trade with ease. Whether you're looking to showcase your own collection or discover rare and exciting models, our site makes the process simple and enjoyable. Clients can browse a curated inventory of high‑quality diecast cars, connect with fellow collectors, and find the perfect pieces to expand their collection. With a smooth user experience and a community-driven spirit, we’re the go‑to destination for anyone passionate about diecast cars.

Target Market(s)

diecast collectors

Industry/Entity Type

Diecast Collectables

Coding

Coded - Design and coding required

Number of Pages Required

3 page

Font styles to use
Sans Serif

Colors
EE7325
F08F49
F5BC92
FAE3D3
FDF4ED

Requirements
Must have
• Cool look and feel. Woo commerce page to post and sell my inventory
Nice to have
• page for users to post their cars or looking for trades.
Should not have
• look cheap

```html
<!DOCTYPE html>
<html lang="en">
<head>
<meta charset="utf-8">
<title>Brimble Diecast Torvel Collectables</title>
<link href="https://fonts.googleapis.com/css2?family=Poppins:wght@400;500;600;700;800&display=swap" rel="stylesheet">
<style>
:root{
  --orange:#EE7325;
  --orange-2:#F08F49;
  --peach:#F5BC92;
  --blush:#FAE3D3;
  --cream:#FDF4ED;
  --ink:#3a3a3a;
  --text:#4a4a4a;
  --dark:#2f2f2f;
  --white:#ffffff;
}
*{box-sizing:border-box;margin:0;padding:0}
html,body{width:1200px;height:3474px;overflow:hidden}
body{font-family:'Poppins',sans-serif;color:var(--text);background:var(--white);position:relative}
.btn{position:absolute;display:flex;align-items:center;justify-content:center;border-radius:30px;font-weight:600;font-size:14px;text-transform:uppercase;text-decoration:none;white-space:nowrap}
.btn-solid{background:linear-gradient(180deg,var(--orange-2),var(--orange));color:var(--white)}
.btn-outline{border:1.5px solid var(--orange);color:var(--orange);background:var(--white)}
.accent{color:var(--orange)}
.section-title{font-weight:700;color:var(--ink);text-transform:uppercase;white-space:nowrap}

/* hero */
.hero{position:absolute;left:0;top:0;width:1200px;height:651px;overflow:hidden;background:#2a241f}
.hero-photo{position:absolute;inset:0;
  background:
    radial-gradient(ellipse 330px 90px at 560px 300px,rgba(238,115,37,.55) 0%,rgba(238,115,37,0) 70%),
    radial-gradient(ellipse 420px 140px at 560px 270px,#3f6672 0%,#34505a 40%,rgba(52,80,90,0) 75%),
    radial-gradient(ellipse 160px 120px at 40px 400px,rgba(120,40,35,.6) 0%,rgba(120,40,35,0) 70%),
    radial-gradient(ellipse 700px 260px at 600px 560px,#5e5348 0%,rgba(94,83,72,0) 80%),
    radial-gradient(ellipse 900px 500px at 600px 200px,#4a3f36 0%,#2f2823 60%,#1d1916 100%)}
.hero-shade{position:absolute;inset:0;background:linear-gradient(180deg,rgba(0,0,0,.35) 0%,rgba(0,0,0,0) 30%,rgba(0,0,0,.15) 60%,rgba(40,30,25,.35) 100%)}
.brand{position:absolute;left:74px;top:60px;display:flex;align-items:center;gap:10px;color:var(--white);font-weight:700;font-size:17px;line-height:1.15}
.brand-dot{flex:none;width:22px;height:22px;border-radius:50%;background:var(--orange)}
.nav{position:absolute;top:109px;left:0;width:1200px;height:22px}
.nav a{position:absolute;color:var(--white);font-weight:600;font-size:15px;text-decoration:none;text-transform:uppercase;white-space:nowrap}
.nav a.active{color:var(--orange)}
.hero h1{position:absolute;top:356px;left:0;width:1200px;text-align:center;color:var(--white);font-weight:800;font-size:44px;line-height:50px;text-transform:uppercase;text-shadow:0 2px 10px rgba(0,0,0,.4)}

/* welcome */
.welcome-title{position:absolute;top:712px;left:0;width:1200px;text-align:center;font-size:31px;line-height:36px}
.welcome-text{position:absolute;top:798px;left:160px;width:880px;text-align:center;font-size:17px;line-height:28px}

/* featured */
.featured{position:absolute;left:0;top:1011px;width:1200px;height:523px;background:linear-gradient(180deg,#f3ece4 0%,#f6e3d2 55%,#f1d3b9 100%)}
.featured-title{position:absolute;left:74px;top:1082px;font-size:31px}
.arrow{position:absolute;top:1090px;width:26px;height:26px;border-radius:50%}
.view-more{position:absolute;left:941px;top:1091px;width:185px;text-align:right;color:var(--orange);font-size:12.5px;font-weight:600;text-decoration:underline;text-transform:uppercase;white-space:nowrap}
.card{position:absolute;top:1147px;width:243px}
.card-img{width:243px;height:171px;border-radius:8px}
.card h3{margin-top:17px;font-size:14px;font-weight:700;color:var(--ink);text-transform:uppercase}
.card p{margin-top:4px;font-size:14px;line-height:21px}
.card .btn{top:266px;height:37px;font-size:14px;text-transform:none}

/* why */
.frame-back{position:absolute;background:var(--blush);border-radius:40px}
.frame-img{position:absolute;border-radius:30px}
.why-title{position:absolute;left:616px;top:1642px;font-size:31px}
.why-text{position:absolute;left:616px;top:1690px;width:512px;font-size:17px;line-height:29px}

/* services */
.services{position:absolute;left:0;top:2009px;width:1200px;height:427px;background:var(--cream)}
.svc{position:absolute;top:2119px;width:328px;height:243px;background:var(--white);border-radius:30px;text-align:center}
.svc-icon{position:absolute;left:122px;top:13px;width:84px;height:84px;border-radius:50%;background:var(--orange);box-shadow:0 0 0 5px var(--blush);display:flex;align-items:center;justify-content:center}
.svc h3{position:absolute;top:108px;left:0;width:100%;font-size:18.5px;font-weight:700;color:var(--ink)}
.svc p{position:absolute;top:142px;left:22px;width:284px;font-size:13.5px;line-height:22px}

/* blog */
.blog-title{position:absolute;top:2494px;left:0;width:1200px;text-align:center;font-size:31px}
.post-main h3{position:absolute;left:74px;top:2922px;width:520px;font-size:19px;line-height:29px;font-weight:700;color:var(--ink);text-transform:uppercase}
.post-main p{position:absolute;left:74px;top:2982px;width:510px;font-size:14px;line-height:22px}
.read{position:absolute;color:var(--orange);font-weight:600;font-size:15px;text-decoration:underline;white-space:nowrap}
.post{position:absolute;left:616px;width:510px;height:155px}
.post-img{position:absolute;left:0;top:0;width:224px;height:155px;border-radius:20px}
.post h3{position:absolute;left:247px;top:0;width:263px;font-size:18px;line-height:25px;font-weight:700;color:var(--ink);text-transform:uppercase}
.post p{position:absolute;left:247px;font-size:14px;line-height:23px;width:263px}

/* footer */
.footer{position:absolute;left:0;top:3170px;width:1200px;height:304px;background:var(--dark);color:var(--white)}
.footer h4{position:absolute;top:50px;font-size:19px;font-weight:600;text-transform:uppercase;white-space:nowrap}
.footer a,.footer span.f-line{position:absolute;font-size:14.5px;color:var(--white);text-decoration:none;white-space:nowrap}
.f-brand{position:absolute;left:96px;top:70px;width:200px;display:flex;flex-direction:column;align-items:center;gap:12px;font-weight:700;font-size:20px;line-height:1.2;text-align:center}
.f-brand .brand-dot{width:60px;height:60px}
.f-copy{position:absolute;left:60px;top:206px;width:272px;text-align:center;font-size:13px;line-height:21px}
.email-box{position:absolute;left:886px;top:146px;width:240px;height:49px;border:1px solid #777;border-radius:25px}
.email-box .f-line{left:22px;top:15px;font-size:13px}
.social{position:absolute;top:224px;width:22px;height:22px;border-radius:50%;border:2px solid var(--white)}
</style>
</head>
<body>

<header class="hero">
  <div class="hero-photo" role="img" aria-label="Photo of a weathered blue muscle car model with flame paint in a dark workshop"></div>
  <div class="hero-shade"></div>
  <div class="brand"><span class="brand-dot"></span><span>Brimble<br>Diecast</span></div>
  <a class="btn btn-solid" style="left:650px;top:38px;width:243px;height:50px">Browse Our Inventory</a>
  <a class="btn btn-solid" style="left:909px;top:38px;width:217px;height:50px">List Your Own Cars</a>
  <nav class="nav">
    <a class="active" style="left:264px">Home</a>
    <a style="left:346px">About</a>
    <a style="left:435px">Inventory</a>
    <a style="left:559px">Buy / Sell / Trade</a>
    <a style="left:735px">Community</a>
    <a style="left:867px">Blog</a>
    <a style="left:946px">FAQ's</a>
    <a style="left:1029px">Contact Us</a>
  </nav>
  <h1>Your Marketplace<br>for Miniature Masterpieces</h1>
  <a class="btn btn-solid" style="left:479px;top:481px;width:244px;height:50px">Browse Our Inventory</a>
</header>

<h2 class="welcome-title section-title">Welcome to <span class="accent">Brimble Diecast</span><br><span class="accent">Torvel Collectables</span></h2>
<p class="welcome-text">Welcome to the ultimate hub for diecast collectors. Explore a growing marketplace where you can buy, sell, or trade your favorite models with collectors from around the world.</p>
<a class="btn btn-outline" style="left:519px;top:884px;width:161px;height:49px">Learn More</a>

<section class="featured" role="img" aria-label="Faded desert landscape background"></section>
<h2 class="featured-title section-title">Featured <span class="accent">Inventory</span></h2>
<svg class="arrow" style="left:459px" viewBox="0 0 26 26"><circle cx="13" cy="13" r="13" fill="#b9b2ab"/><path d="M15 7l-6 6 6 6M9 13h10" stroke="#fff" stroke-width="2.5" fill="none"/></svg>
<svg class="arrow" style="left:497px" viewBox="0 0 26 26"><circle cx="13" cy="13" r="13" fill="#333"/><path d="M11 7l6 6-6 6M7 13h10" stroke="#fff" stroke-width="2.5" fill="none"/></svg>
<a class="view-more">View More Inventory</a>

<div class="card" style="left:74px">
  <div class="card-img" role="img" aria-label="Green and yellow classic sports car model" style="background:linear-gradient(135deg,#7a6a50,#3f7a3a 50%,#c9b23a)"></div>
  <h3>Excepteur Sint</h3><p>Nemo enim ipsam voluptatem quia voluptas sit.</p>
  <a class="btn btn-solid" style="left:0;width:117px">Quick View</a>
  <a class="btn btn-outline" style="left:124px;width:119px">Wishlist</a>
</div>
<div class="card" style="left:344px">
  <div class="card-img" role="img" aria-label="Red and white race car model with flame livery" style="background:linear-gradient(135deg,#3b3030,#c8403a 50%,#e8e0d8)"></div>
  <h3>Excepteur Sint</h3><p>Nemo enim ipsam voluptatem quia voluptas sit.</p>
  <a class="btn btn-solid" style="left:0;width:117px">Quick View</a>
  <a class="btn btn-outline" style="left:124px;width:119px">Wishlist</a>
</div>
<div class="card" style="left:615px">
  <div class="card-img" role="img" aria-label="Yellow race car model on display" style="background:linear-gradient(135deg,#6a5e52,#e0c23a 50%,#4a4038)"></div>
  <h3>Excepteur Sint</h3><p>Nemo enim ipsam voluptatem quia voluptas sit.</p>
  <a class="btn btn-solid" style="left:0;width:117px">Quick View</a>
  <a class="btn btn-outline" style="left:124px;width:119px">Wishlist</a>
</div>
<div class="card" style="left:883px">
  <div class="card-img" role="img" aria-label="Red, white and blue prototype race car model" style="background:linear-gradient(135deg,#d8d2c8,#2b3e8a 50%,#b83a3a)"></div>
  <h3>Excepteur Sint</h3><p>Nemo enim ipsam voluptatem quia voluptas sit.</p>
  <a class="btn btn-solid" style="left:0;width:117px">Quick View</a>
  <a class="btn btn-outline" style="left:124px;width:119px">Wishlist</a>
</div>

<div class="frame-back" style="left:74px;top:1604px;width:512px;height:328px"></div>
<div class="frame-img" role="img" aria-label="Packaged toy cars on a store shelf" style="left:94px;top:1623px;width:474px;height:290px;background:linear-gradient(120deg,#2f6fb8,#e2a53a 45%,#3a4f8a)"></div>
<h2 class="why-title section-title">Why <span class="accent">Choose Us?</span></h2>
<p class="why-text">We bring together passionate collectors and<br>high quality diecast cars in one trusted space. Whether you're hunting for rare finds or looking to give your collection a new home, our platform makes every transaction smooth and secure.</p>
<a class="btn btn-outline" style="left:616px;top:1846px;width:162px;height:48px">Learn More</a>

<section class="services"></section>
<div class="svc" style="left:74px">
  <div class="svc-icon"><svg width="44" height="44" viewBox="0 0 44 44" fill="none" stroke="#fff" stroke-width="2.5"><path d="M4 8h6l5 20h20l4-14H13"/><circle cx="17" cy="35" r="3"/><circle cx="32" cy="35" r="3"/><path d="M22 18l3 3 6-6"/></svg></div>
  <h3>BUYING</h3>
  <p>Browse verified listings from collectors worldwide. Each listing includes detailed descriptions and photos so you can shop with confidence.</p>
</div>
<div class="svc" style="left:437px">
  <div class="svc-icon"><svg width="44" height="44" viewBox="0 0 44 44" fill="none" stroke="#fff" stroke-width="2.5"><path d="M24 6h14v14L20 38 6 24z"/><circle cx="31" cy="13" r="2.5"/></svg></div>
  <h3>SELLING</h3>
  <p>Turn your collection into cash. List your diecast cars in minutes with our simple selling tools and reach thousands of collectors instantly.</p>
</div>
<div class="svc" style="left:798px">
  <div class="svc-icon"><svg width="44" height="44" viewBox="0 0 44 44" fill="none" stroke="#fff" stroke-width="2.5"><path d="M6 38h32M10 38V28h5v10M20 38V22h5v10M30 38V14h5v24M8 20l10-8 7 5 11-10"/></svg></div>
  <h3>TRADING</h3>
  <p>Prefer to swap? Connect with other collectors and trade models securely through our built in messaging and trade offer system.</p>
</div>

<h2 class="blog-title section-title">Blog <span class="accent">Articles</span></h2>
<div class="frame-back" style="left:74px;top:2572px;width:512px;height:329px"></div>
<div class="frame-img" role="img" aria-label="Red and blue muscle car models on a street with bokeh lights" style="left:94px;top:2592px;width:474px;height:291px;background:linear-gradient(120deg,#9a8c80,#b33a30 40%,#3a5fa8 70%,#6a6058)"></div>
<div class="post-main">
  <h3>Top 10 Rare Diecast Cars Every<br>Collector Wants</h3>
  <p>Nemo enim ipsam voluptatem quia voluptas sit aspernatur aut odit aut fugit, sed quia consequuntur magni dolores eos qui ratione voluptatem sequi nesciunt.</p>
  <a class="read" style="left:74px;top:3055px">Read More</a>
</div>

<div class="post" style="top:2573px">
  <div class="post-img" role="img" aria-label="Colorful race car model" style="background:linear-gradient(135deg,#444,#3a9a4a 40%,#e07a2a 70%,#555)"></div>
  <h3>How to Spot Authentic vs. Replica Diecast Models</h3>
  <p style="top:85px">Nemo enim ipsam voluptatem quia voluptas sit aspernatur aut.</p>
  <a class="read" style="left:247px;top:136px">Read More</a>
</div>
<div class="post" style="top:2759px">
  <div class="post-img" role="img" aria-label="Shelves of diecast car models" style="background:linear-gradient(135deg,#3a4048,#c86a3a 50%,#4a5a68)"></div>
  <h3>Beginner's Guide to Starting a Diecast Collection</h3>
  <p style="top:85px">Nemo enim ipsam voluptatem quia voluptas sit aspernatur aut.</p>
  <a class="read" style="left:247px;top:136px">Read More</a>
</div>
<div class="post" style="top:2935px">
  <div class="post-img" role="img" aria-label="Wooden display case with car models" style="background:linear-gradient(135deg,#c8a078,#e8d8c0 50%,#b8463a)"></div>
  <h3>How to Properly Store and Display Your Diecast Cars</h3>
  <p style="top:85px">Nemo enim ipsam voluptatem quia voluptas sit aspernatur aut.</p>
  <a class="read" style="left:247px;top:136px">Read More</a>
</div>

<footer class="footer">
  <div class="f-brand"><span class="brand-dot"></span><span>Brimble Diecast</span></div>
  <p class="f-copy">Copyright © 2026 Company Name<br>All Right Reserved</p>
  <h4 style="left:342px">Quick Links</h4>
  <a style="left:342px;top:88px">Home</a>
  <a style="left:342px;top:121px">About</a>
  <a style="left:342px;top:154px">Inventory</a>
  <a style="left:342px;top:187px">Buy / Sell / Trade</a>
  <a style="left:342px;top:220px">Community</a>
  <a style="left:499px;top:88px">Blog</a>
  <a style="left:499px;top:121px">FAQ's</a>
  <a style="left:499px;top:154px">Contact Us</a>
  <h4 style="left:619px">Contact Info</h4>
  <span class="f-line" style="left:619px;top:88px;line-height:27px">48 Larkspur Row Suite 12,<br>Fenwick 20417</span>
  <span class="f-line" style="left:619px;top:147px">+1-555-014-2290</span>
  <span class="f-line" style="left:619px;top:175px">hello@brimblediecast.example</span>
  <div class="social" style="left:611px"></div>
  <div class="social" style="left:641px"></div>
  <div class="social" style="left:681px"></div>
  <div class="social" style="left:721px"></div>
  <div class="social" style="left:761px"></div>
  <h4 style="left:886px">Newsletter</h4>
  <span class="f-line" style="left:886px;top:88px;line-height:23px">Nemo enim ipsam voluptatem<br>quia voluptas sit.</span>
  <div class="email-box"><span class="f-line">Email Address</span>
    <svg style="position:absolute;right:14px;top:15px" width="18" height="18" viewBox="0 0 18 18" fill="none" stroke="#EE7325" stroke-width="1.6"><path d="M2 9l14-7-5 14-3-6z"/></svg>
  </div>
</footer>

</body>
</html>
```